New business Cards

We need some new cards that stand out. We love our logo and colour scheme but need to incorporate a qubo logo and bfn logo yet still keep our cards uncluttered and clean looking.
Our tag is Bright Ledger. Anywhere, Anytime.
The idea of the cards is to show authority in accounting and Qubo/ cloud software

```html
<!DOCTYPE html>
<html lang="en">
<head>
<meta charset="utf-8">
<title>Fenwick – Business Cards</title>
<link href="https://fonts.googleapis.com/css2?family=Mulish:wght@800&family=Open+Sans:wght@400;600&family=Lobster&display=swap" rel="stylesheet">
<style>
  :root {
    --backdrop: #e9e4dc;
    --card-white: #ffffff;
    --brand-green: #6dbe45;
    --lime: #a6d04a;
    --soft-green: #c4e3a6;
    --ink: #231f20;
    --text: #2b2b2b;
    --badge-blue: #1aa8e0;
    --badge-teal: #1f8fa6;
    --badge-navy: #1d5aa6;
  }
  * { margin: 0; padding: 0; box-sizing: border-box; }
  html, body {
    width: 1200px; height: 900px; overflow: hidden;
    background: var(--backdrop);
  }
  .canvas { position: relative; width: 1200px; height: 900px; }

  .card {
    position: absolute; left: 250px; width: 700px; height: 400px;
    overflow: hidden;
    box-shadow: 0 6px 18px rgba(0,0,0,0.18);
  }
  .card--front { top: 30px; background: var(--card-white); }
  .card--back { top: 470px; background: var(--brand-green); }

  /* front */
  .front-wash {
    position: absolute; inset: 0 0 auto 0; height: 190px;
    background: linear-gradient(100deg, var(--brand-green) 0%, var(--soft-green) 28%, var(--card-white) 58%);
  }
  .wordmark {
    position: absolute; display: flex; align-items: center; gap: 10px;
    font-family: "Open Sans", sans-serif; font-weight: 600;
    color: var(--brand-green); letter-spacing: 3px;
  }
  .wordmark__square { background: var(--brand-green); }
  .card--front .wordmark { top: 28px; right: 36px; font-size: 26px; }
  .card--front .wordmark__square { width: 34px; height: 34px; }

  .role-band {
    position: absolute; top: 112px; left: 430px; width: 270px; height: 52px;
    background: var(--ink);
    clip-path: polygon(40px 0, 100% 0, 100% 100%, 0 100%);
    color: #fff; font-family: "Open Sans", sans-serif; font-size: 22px;
    display: flex; align-items: center; padding-left: 70px;
  }
  .name-band {
    position: absolute; top: 158px; left: 0; width: 490px; height: 56px;
    background: var(--lime);
    clip-path: polygon(0 0, 100% 0, calc(100% - 46px) 100%, 0 100%);
    display: flex; align-items: center; padding-left: 36px;
    font-family: "Mulish", sans-serif; font-weight: 800; font-size: 30px; color: var(--ink);
  }
  .name-band__credentials {
    font-family: "Open Sans", sans-serif; font-weight: 400; font-size: 18px; margin-left: 8px;
  }
  .badges { position: absolute; top: 176px; right: 20px; width: 110px; height: 90px; }

  .contact {
    position: absolute; top: 232px; left: 40px;
    font-family: "Open Sans", sans-serif; font-size: 25px; line-height: 38px; color: var(--text);
    list-style: none;
  }

  /* back */
  .light-band {
    position: absolute; top: 120px; left: 0; width: 100%; height: 150px;
    background: linear-gradient(90deg, var(--brand-green) 0%, #ffffff 32%, #ffffff 62%, var(--brand-green) 100%);
  }
  .card--back .wordmark {
    top: 168px; left: 50%; transform: translateX(-50%); font-size: 38px;
  }
  .card--back .wordmark__square { width: 48px; height: 48px; }
  .tagline {
    position: absolute; bottom: 32px; left: 40px;
    font-family: "Lobster", cursive; font-size: 38px; color: #fff;
  }
</style>
</head>
<body>
<main class="canvas">

  <section class="card card--front">
    <div class="front-wash"></div>
    <div class="wordmark"><span class="wordmark__square"></span>FENWICK</div>
    <div class="role-band">Partner</div>
    <div class="name-band">Elena Marsh<span class="name-band__credentials">, BFN, CTA</span></div>
    <svg class="badges" viewBox="0 0 110 90" aria-label="Partner badges">
      <circle cx="30" cy="18" r="16" fill="var(--badge-blue)"/>
      <circle cx="66" cy="18" r="16" fill="var(--badge-teal)"/>
      <rect x="10" y="42" width="90" height="44" fill="var(--badge-navy)"/>
    </svg>
    <ul class="contact">
      <li>Brookvale Vic 3799</li>
      <li>p: 03 5550 1234</li>
      <li>e: elenam@fenwickbiz.com.au</li>
      <li>www.fenwickbiz.com.au</li>
    </ul>
  </section>

  <section class="card card--back">
    <div class="light-band"></div>
    <div class="wordmark"><span class="wordmark__square"></span>FENWICK</div>
    <p class="tagline">Bright Ledger. Anywhere, Anytime.</p>
  </section>

</main>
</body>
</html>
```